Brochure Design Project

Please design a brochure(trifold) like the picture below (MAKE IT UNIQUE AND INTERESTING WITH PICTURES, CARTOONS that can represent our software)
**the brochure you will be designing in English, but we plan to make the same brochure in Indonesian as well.
Try to convey and convince to the readers that cloud computing of Lumatrek will be able to help them to be more efficient.
give them access from anywhere in the world, safety and so on.
Other details are on the attachment
Updates
Hi,
Please dont use the pictures that i stated you can use for "ideas".
Those have the name of other companies in them. Please find similar and fresh pictures to be used on the brochure.
You can also include pictures from the ppt attached

```html
<!DOCTYPE html>
<html lang="en">
<head>
<meta charset="utf-8">
<title>Lumatrek Trifold Brochure</title>
<link href="https://fonts.googleapis.com/css2?family=Open+Sans:wght@400;600;700&family=Oswald:wght@500;600&family=Montserrat:wght@700&display=swap" rel="stylesheet">
<style>
  :root{
    --stage:#e9e9ec;
    --navy:#1f2c5e;
    --navy-deep:#18234d;
    --blue-glow:#3d7fd6;
    --accent-blue:#2f7fd8;
    --text-light:#ffffff;
    --text-dark:#333333;
    --call-blue:#1f6fc1;
    --call-bg:#e6e7ea;
    --orange:#f5a623;
    --swoosh:#8f959f;
    --logo-green:#5a9a3a;
  }
  *{box-sizing:border-box;margin:0;padding:0}
  html,body{width:1200px;height:960px;overflow:hidden;background:var(--stage)}
  .brochure{position:absolute;left:0;top:55px;width:1200px;height:849px;display:flex}
  .panel{position:relative;width:400px;height:849px;overflow:hidden}

  /* inside panel */
  .panel--inside{background:linear-gradient(180deg,var(--navy) 0%,var(--navy-deep) 100%);color:var(--text-light);font-family:"Open Sans",sans-serif}
  .section-title{position:absolute;left:8px;display:flex;align-items:center;gap:8px;font-family:"Oswald",sans-serif;font-weight:500;font-size:21px;letter-spacing:.2px}
  .section-title .lead{font-size:27px;font-weight:600}
  .section-title svg{flex:none}
  .beliefs{position:absolute;left:38px;top:80px;width:320px;list-style:none;font-size:15.5px;line-height:20px}
  .beliefs li{position:relative;padding-left:20px;margin-bottom:9px}
  .beliefs li::before{content:"";position:absolute;left:0;top:6px;width:8px;height:8px;border:2px solid #fff;border-radius:50%}
  .profile{position:absolute;left:42px;top:380px;width:346px;font-size:12.5px;line-height:14.5px;text-align:justify}
  .profile p{margin-bottom:14px}
  .inside-photo{position:absolute;left:0;top:590px;width:400px;height:259px}

  /* back panel */
  .panel--back{background:#fff;color:var(--text-dark);font-family:"Open Sans",sans-serif;text-align:center}
  .back-photo{position:absolute;left:0;top:0;width:330px;height:228px;background:linear-gradient(90deg,#2b6fc4 0%,#6fb3ee 40%,#dfe6ee 70%,#f4f4f4 100%)}
  .back-photo-edge{position:absolute;left:0;top:228px;width:330px;height:4px;background:var(--navy)}
  .contact-title{position:absolute;left:0;right:0;top:290px;font-size:26px;font-weight:700;color:#3a3a3a}
  .contact-title span{display:inline-block;border-bottom:2px solid #3a3a3a;padding:0 4px 2px}
  .contact-lines{position:absolute;left:0;right:0;top:340px;font-size:18px;line-height:25px}
  .address-title{position:absolute;left:0;right:0;top:410px;font-size:18px;font-weight:600}
  .address{position:absolute;left:0;right:0;top:437px;font-size:18px;line-height:22px}
  .fax{position:absolute;left:0;right:0;top:507px;font-size:18px}
  .company-mark{position:absolute;left:0;right:0;top:615px;display:flex;justify-content:center;align-items:center;gap:10px}
  .company-mark .dot{width:50px;height:50px;border-radius:50%;background:var(--logo-green)}
  .company-mark .name{font-size:22px;font-weight:600;color:#4a4a4a;letter-spacing:1px}
  .call-box{position:absolute;left:40px;top:690px;width:334px;height:123px;border-radius:8px;background:var(--call-bg);color:var(--call-blue);font-weight:700;padding-top:14px}
  .call-box .label{font-size:38px;line-height:46px}
  .call-box .number{font-size:38px;line-height:48px}

  /* front panel */
  .panel--front{background:radial-gradient(ellipse 360px 300px at 380px 360px,var(--blue-glow) 0%,#2c4e9a 45%,var(--navy) 80%);color:var(--text-light)}
  .front-photo{position:absolute;left:0;top:0;width:400px;height:350px}
  .brand-title{position:absolute;left:0;right:0;top:430px;text-align:center;font-family:"Montserrat",sans-serif;font-weight:700;font-size:52px;letter-spacing:4px}
  .tagline{position:absolute;left:0;right:0;top:550px;text-align:center;font-family:"Oswald",sans-serif;font-weight:600;line-height:54px}
  .tagline .t1{display:block;font-size:44px;color:#e8eaf2}
  .tagline .t1 small{font-size:30px}
  .tagline .t2{display:block;font-size:48px;color:var(--orange);letter-spacing:5px}
  .badges{position:absolute;left:48px;top:772px;display:flex;gap:26px;align-items:center}
  .badge{background:#fff;opacity:.95}
  .badge--seal{width:140px;height:58px;border-radius:29px}
  .badge--partner{width:150px;height:50px;border-radius:6px}
</style>
</head>
<body>
<main class="brochure">

  <section class="panel panel--inside">
    <h2 class="section-title" style="top:28px">
      <svg width="30" height="26" viewBox="0 0 30 26"><path d="M2 2l10 11-10 11M14 2l10 11-10 11" fill="none" stroke="var(--accent-blue)" stroke-width="5"/></svg>
      <span><span class="lead">Seven</span> things we believe to be true</span>
    </h2>
    <ul class="beliefs">
      <li>Focus on the user and all else will follow</li>
      <li>Dedication towards automation</li>
      <li>Fast is better than slow</li>
      <li>Innovate, innovate and evolve</li>
      <li>Collaboration and synchrony towards perfection</li>
      <li>Great isn’t good enough</li>
      <li>Gratitude and Appreciation</li>
    </ul>

    <h2 class="section-title" style="top:335px">
      <svg width="30" height="26" viewBox="0 0 30 26"><path d="M2 2l10 11-10 11M14 2l10 11-10 11" fill="none" stroke="var(--accent-blue)" stroke-width="5"/></svg>
      <span><span class="lead">Company</span> Profile</span>
    </h2>
    <div class="profile">
      <p>Lumatrek was created to meet the needs of entrepreneurs who want to access their company’s finances with ease.</p>
      <p>Norvale Technology was established in 2011 in Jakarta, with a mission to make business automation that will enhance the quality and efficiency of businesses.</p>
      <p>All of us at Norvale Technology aim to provide best user experience to our clients.</p>
      <p>Norvale Technology is always innovating and evolving</p>
    </div>

    <svg class="inside-photo" viewBox="0 0 400 259" role="img" aria-label="Photo of a smiling businesswoman beside a tablet showing finance charts">
      <defs>
        <linearGradient id="insidePhotoFill" x1="0" y1="0" x2="1" y2="0">
          <stop offset="0" stop-color="#b9a08e"/><stop offset=".45" stop-color="#dcd6d0"/><stop offset="1" stop-color="#eef1f5"/>
        </linearGradient>
      </defs>
      <path d="M0 95 Q170 20 400 40 L400 259 L0 259Z" fill="var(--swoosh)"/>
      <path d="M0 112 Q170 38 400 58 L400 259 L0 259Z" fill="url(#insidePhotoFill)"/>
    </svg>
  </section>

  <section class="panel panel--back">
    <div class="back-photo" role="img" aria-label="Photo of a woman touching a floating transparent software screen"></div>
    <div class="back-photo-edge"></div>

    <h2 class="contact-title"><span>Contact us</span></h2>
    <p class="contact-lines">Customer support &amp; feedback<br>support@lumatrek.com</p>
    <h3 class="address-title">Office Address</h3>
    <p class="address">Harbor Point Plaza Block C #. 14<br>Jl. Cedar Lane No. 21, Kembang,<br>North District, Indonesia</p>
    <p class="fax">Fax: (021) 5550 1743</p>

    <div class="company-mark">
      <span class="dot"></span>
      <span class="name">NORVALE TECHNOLOGY</span>
    </div>

    <div class="call-box">
      <div class="label">Call Us Today</div>
      <div class="number">(021) 5550 1742</div>
    </div>
  </section>

  <section class="panel panel--front">
    <svg class="front-photo" viewBox="0 0 400 350" role="img" aria-label="Photo of a woman working on a laptop in a bright office">
      <defs>
        <linearGradient id="frontPhotoFill" x1="0" y1="0" x2="0" y2="1">
          <stop offset="0" stop-color="#f2f3f5"/><stop offset=".6" stop-color="#c9ccd2"/><stop offset="1" stop-color="#9aa0a8"/>
        </linearGradient>
      </defs>
      <path d="M0 0 H400 V250 Q230 380 0 240Z" fill="url(#frontPhotoFill)"/>
      <path d="M0 240 Q230 380 400 250 L400 270 Q230 400 0 262Z" fill="var(--swoosh)"/>
    </svg>

    <h1 class="brand-title">Lumatrek</h1>
    <p class="tagline">
      <span class="t1">AUTOMATE <small>YOUR</small></span>
      <span class="t2">BUSINESSES</span>
    </p>

    <div class="badges">
      <span class="badge badge--seal" role="img" aria-label="Security certificate badge"></span>
      <span class="badge badge--partner" role="img" aria-label="Cloud hosting partner badge"></span>
    </div>
  </section>

</main>
</body>
</html>
```